Author and Publisher

Cover for a book on the process of publishing a book from the presentation to the publisher until the selling in bookstores :
A behind-the-scenes journey through the world of book publishing, from manuscript to bookstore. The book explores the relationship between authors and publishers, manuscript selection, contracts, editing, proofreading, book design, printing, distribution, bookstores and online sales. It reveals the many people, decisions and processes involved in turning a text into a physical book and bringing it to readers. The illustration should evoke publishing as a lively, contemporary ecosystem, combining creativity, craftsmanship, business and the enduring appeal of books.
FORMAT : 14 x 20,5 cm
AUTHOR : Luc Varennes
TITLE : Le scribe et la presse
PUBLISHER : Editions Trovel (at the bottom of the page)
Target Market(s)
General public, mainly news authors of books
Look and feel
Each slider illustrates characteristics of the customer's brand and the style your logo design should communicate.

```html
<!DOCTYPE html>
<html lang="fr">
<head>
<meta charset="utf-8">
<title>Le scribe et la presse — Luc Varennes</title>
<link rel="stylesheet" href="https://fonts.googleapis.com/css2?family=Bebas+Neue&display=swap">
<style>
  :root {
    --backdrop: #808080;
    --paper: #ffffff;
    --ink: #272d35;
    --band-navy: #03203d;
    --band-teal: #1790ac;
    --band-slate: #2a2e34;
    --author-text: #ffffff;
    --publisher-text: #dfeef3;
  }
  html, body {
    margin: 0;
    padding: 0;
    width: 1200px;
    height: 1199px;
    overflow: hidden;
    background: var(--backdrop);
  }
  .book-cover {
    position: absolute;
    left: 244px;
    top: 90px;
    width: 710px;
    height: 1017px;
    background: var(--paper);
    overflow: hidden;
  }
  .cover-art {
    display: block;
    width: 710px;
    height: 1017px;
  }
  .title-line,
  .author-name,
  .publisher-name {
    font-family: "Bebas Neue", "Oswald", sans-serif;
  }
  .title-line { fill: var(--ink); }
  .title-rule { fill: var(--ink); }
  .author-name { fill: var(--author-text); }
  .publisher-name { fill: var(--publisher-text); letter-spacing: 3px; }
</style>
</head>
<body>
  <main class="book-cover">
    <svg class="cover-art" viewBox="0 0 710 1017" xmlns="http://www.w3.org/2000/svg">
      <defs>
        <linearGradient id="band-gradient" x1="0" y1="0" x2="1" y2="0">
          <stop offset="0" stop-color="var(--band-navy)"/>
          <stop offset="0.08" stop-color="var(--band-navy)"/>
          <stop offset="0.48" stop-color="var(--band-teal)"/>
          <stop offset="0.93" stop-color="var(--band-slate)"/>
          <stop offset="1" stop-color="var(--band-slate)"/>
        </linearGradient>
      </defs>

      <g class="cover-title" aria-label="Le scribe et la presse">
        <text class="title-line" x="40" y="294" font-size="255" textLength="630" lengthAdjust="spacingAndGlyphs">LE SCRIBE</text>
        <rect class="title-rule" x="40" y="412" width="222" height="24"/>
        <text class="title-line" x="343" y="502" font-size="220" text-anchor="middle">ET</text>
        <rect class="title-rule" x="452" y="412" width="218" height="24"/>
        <text class="title-line" x="40" y="718" font-size="255" textLength="630" lengthAdjust="spacingAndGlyphs">LA PRESSE</text>
      </g>

      <rect class="author-band" x="0" y="838" width="710" height="179" fill="url(#band-gradient)"
        role="img" aria-label="Bande illustrée aux tons bleu nuit et turquoise, silhouette découpée en haut"/>

      <text class="author-name" x="355" y="958" font-size="86" text-anchor="middle" textLength="440" lengthAdjust="spacingAndGlyphs">LUC VARENNES</text>
      <text class="publisher-name" x="355" y="998" font-size="24" text-anchor="middle">EDITIONS TROVEL</text>
    </svg>
  </main>
</body>
</html>
```